Flyer for Aluminium recycling business

We are a startup aluminium recycling business. We don’t have a logo yet. I’ve attached a flyer created by one of our sales people but it’s a bit average and we need something a bit more modern and slick. You have creative license to completely change everything - as long as the information being communicated is the same.

Target Market(s)

Hospitality, Hotels, Apartment blocks, malls etcs

Industry/Entity Type

Aluminium recycling

Requirements
Must have
• the wording
Nice to have
• you have free license on design aspect

```html
<!DOCTYPE html>
<html lang="en">
<head>
<meta charset="utf-8">
<title>Brightcycle Metals – Aluminium Recycling Flyer</title>
<link href="https://fonts.googleapis.com/css2?family=Poppins:wght@500;600;700&display=swap" rel="stylesheet">
<style>
  :root {
    --forest: #2c3b1f;
    --leaf: #76b843;
    --lime: #7dc142;
    --paper: #f1f1f0;
    --band: #e2e2e2;
    --ink: #1c1c1c;
    --arc-grey: #d6d6d6;
    --white: #ffffff;
  }
  * { margin: 0; padding: 0; box-sizing: border-box; }
  html, body { width: 961px; height: 1200px; overflow: hidden; background: var(--paper); }
  body { font-family: "Poppins", sans-serif; color: var(--ink); }
  .flyer { position: relative; width: 961px; height: 1200px; background: var(--paper); overflow: hidden; }

  .header-band { position: absolute; left: 0; top: 0; width: 961px; height: 240px; background: var(--forest); }
  .shapes { position: absolute; left: 0; top: 0; }

  .brand { position: absolute; left: 0; top: 30px; width: 961px; display: flex; justify-content: center; align-items: center; gap: 10px; }
  .brand-dot { width: 22px; height: 22px; border-radius: 50%; background: var(--leaf); }
  .brand-name { font-weight: 600; font-size: 31px; color: var(--forest); letter-spacing: 0.2px; }

  .headline { position: absolute; left: 0; top: 104px; width: 961px; text-align: center; font-weight: 700; line-height: 49px; font-size: 47px; }
  .headline .line-green { color: var(--lime); display: block; }
  .headline .line-white { color: var(--white); display: block; }

  .tagline { position: absolute; left: 196px; top: 226px; width: 781px; height: 65px; margin-left: -106px; background: var(--leaf); border-radius: 6px; color: var(--white); font-weight: 600; font-size: 19.5px; line-height: 24px; text-align: center; padding-top: 8px; }

  .hub-illustration { position: absolute; left: 318px; top: 462px; width: 300px; height: 300px; border-radius: 50%; background: radial-gradient(circle at 50% 50%, #ffffff 0%, #e9f3e0 55%, #bcdca0 100%); }
  .hub-label { position: absolute; left: 0; top: 134px; width: 300px; text-align: center; font-weight: 700; font-size: 16px; color: #2f8a2a; }

  .step { position: absolute; font-weight: 500; font-size: 14.5px; line-height: 18.6px; color: var(--ink); }
  .step-top { left: 330px; top: 316px; width: 300px; text-align: center; }
  .step-right-upper { left: 690px; top: 398px; width: 210px; }
  .step-right-lower { left: 734px; top: 671px; width: 200px; }
  .step-bottom { left: 330px; top: 888px; width: 300px; text-align: center; }
  .step-left-lower { left: 69px; top: 658px; width: 120px; }
  .step-left-upper { left: 69px; top: 400px; width: 200px; }

  .examples-band { position: absolute; left: 0; top: 974px; width: 961px; height: 226px; background: var(--band); }
  .examples-title { position: absolute; left: 240px; top: 955px; width: 488px; height: 55px; background: var(--forest); border-radius: 3px; color: var(--white); font-weight: 600; font-size: 25.5px; text-align: center; line-height: 55px; }
  .examples-list { position: absolute; list-style: none; font-weight: 500; font-size: 14px; }
  .examples-list li { display: flex; align-items: center; gap: 8px; height: 20px; margin-bottom: 12px; }
  .examples-left { left: 57px; top: 1038px; }
  .examples-right { left: 405px; top: 1038px; }
  .tick { width: 22px; height: 22px; flex: none; }
</style>
</head>
<body>
<main class="flyer">
  <div class="header-band"></div>

  <svg class="shapes" width="961" height="1200" viewBox="0 0 961 1200" aria-hidden="true">
    <!-- header tab -->
    <path d="M205,0 C245,0 252,35 268,62 Q285,93 318,93 L645,93 Q678,93 694,62 C710,35 716,0 750,0 Z" fill="var(--white)"/>

    <!-- outer dashed grey arcs -->
    <circle cx="468" cy="612" r="292" fill="none" stroke="var(--arc-grey)" stroke-width="4" stroke-dasharray="118 72" transform="rotate(-72 468 612)"/>

    <!-- green cycle ring -->
    <circle cx="468" cy="612" r="220" fill="none" stroke="var(--leaf)" stroke-width="15"/>

    <!-- arrowheads, clockwise -->
    <g fill="var(--leaf)" stroke="var(--white)" stroke-width="2">
      <polygon points="660,582 716,582 688,628" transform="rotate(-59 468 612)"/>
      <polygon points="660,582 716,582 688,628" transform="rotate(0 468 612)"/>
      <polygon points="660,582 716,582 688,628" transform="rotate(59 468 612)"/>
      <polygon points="660,582 716,582 688,628" transform="rotate(121 468 612)"/>
      <polygon points="660,582 716,582 688,628" transform="rotate(180 468 612)"/>
      <polygon points="660,582 716,582 688,628" transform="rotate(239 468 612)"/>
    </g>

    <!-- step nodes -->
    <g fill="var(--white)" stroke="var(--leaf)" stroke-width="6">
      <circle cx="468" cy="392" r="35"/>
      <circle cx="662" cy="509" r="35"/>
      <circle cx="662" cy="715" r="35"/>
      <circle cx="468" cy="832" r="35"/>
      <circle cx="274" cy="715" r="35"/>
      <circle cx="274" cy="509" r="35"/>
    </g>

    <!-- node icons -->
    <g fill="var(--ink)">
      <!-- bin -->
      <rect x="454" y="378" width="28" height="4" rx="1"/>
      <rect x="463" y="374" width="10" height="4" rx="1"/>
      <path d="M456,384 L480,384 L477,408 L459,408 Z"/>
      <!-- person with bin -->
      <circle cx="655" cy="492" r="4.5"/>
      <rect x="651" y="498" width="9" height="17" rx="2"/>
      <rect x="651" y="514" width="3.5" height="13"/>
      <rect x="656.5" y="514" width="3.5" height="13"/>
      <path d="M660,502 L668,508 L666,510 L659,505 Z"/>
      <path d="M665,513 L679,513 L677,527 L667,527 Z"/>
      <!-- can -->
      <rect x="652" y="696" width="20" height="38" rx="4"/>
      <ellipse cx="662" cy="698" rx="8" ry="2.5" fill="var(--white)"/>
      <!-- truck -->
      <rect x="453" y="818" width="22" height="18" rx="2"/>
      <path d="M475,824 L484,824 L488,830 L488,836 L475,836 Z"/>
      <circle cx="459" cy="839" r="3.5"/>
      <circle cx="481" cy="839" r="3.5"/>
      <rect x="471" y="842" width="8" height="9" rx="1"/>
      <!-- hand with coin and gear -->
      <path d="M258,722 Q266,716 274,720 L284,720 Q288,722 284,725 L274,725 L290,723 Q294,724 291,728 L276,733 L258,731 Z"/>
      <circle cx="266" cy="704" r="5"/>
      <circle cx="280" cy="698" r="4"/>
      <circle cx="290" cy="708" r="6"/>
      <!-- recycling bin -->
      <path d="M261,497 L287,497 L284,526 L264,526 Z"/>
      <rect x="259" y="492" width="30" height="4" rx="1"/>
      <circle cx="286" cy="524" r="5" stroke="var(--white)" stroke-width="1.5"/>
    </g>
  </svg>

  <div class="brand">
    <span class="brand-dot"></span>
    <span class="brand-name">Brightcycle Metals</span>
  </div>

  <h1 class="headline">
    <span class="line-green">PLAYING THE FALT ALUMINIUM</span>
    <span class="line-white">RECYCLING GAME FOR GOOD</span>
  </h1>

  <p class="tagline">Our parteenshis with ynescommon sense mutsal gain and<br>a better tomon</p>

  <div class="hub-illustration" role="img" aria-label="Recycling symbol filled with cans, bottles, cartons and green leaves">
    <span class="hub-label">RECYCLE</span>
  </div>

  <p class="step step-top">We bring you a free bin</p>
  <p class="step step-right-upper">You throw all and any aluminium waste into the bin-no need to super-clean it.</p>
  <p class="step step-right-lower">Try to compact/<br>squash the<br>aluminium as<br>much as possible</p>
  <p class="step step-bottom">We collect the<br>bin at no charge</p>
  <p class="step step-left-lower">We turn the aluminium waste into a desirable resource</p>
  <p class="step step-left-upper">We pay you for<br>however much of that<br>resource your waste has<br>generated and give<br>you a report on<br>that, so you can<br>see how good<br>you are</p>

  <div class="examples-band"></div>
  <h2 class="examples-title">Examples of what we can take</h2>

  <ul class="examples-list examples-left">
    <li><svg class="tick" viewBox="0 0 22 22" aria-hidden="true"><circle cx="11" cy="11" r="9" fill="none" stroke="#2f8a2a" stroke-width="2"/><path d="M6,11 L10,15 L18,5" fill="none" stroke="#2f8a2a" stroke-width="2.6" stroke-linecap="round"/></svg>Used beverage cans - any</li>
    <li><svg class="tick" viewBox="0 0 22 22" aria-hidden="true"><circle cx="11" cy="11" r="9" fill="none" stroke="#2f8a2a" stroke-width="2"/><path d="M6,11 L10,15 L18,5" fill="none" stroke="#2f8a2a" stroke-width="2.6" stroke-linecap="round"/></svg>Tinfoil-scrunched, crusty, burned or dirty</li>
    <li><svg class="tick" viewBox="0 0 22 22" aria-hidden="true"><circle cx="11" cy="11" r="9" fill="none" stroke="#2f8a2a" stroke-width="2"/><path d="M6,11 L10,15 L18,5" fill="none" stroke="#2f8a2a" stroke-width="2.6" stroke-linecap="round"/></svg>Disposable BBQ roasting trays</li>
  </ul>
  <ul class="examples-list examples-right">
    <li><svg class="tick" viewBox="0 0 22 22" aria-hidden="true"><circle cx="11" cy="11" r="9" fill="none" stroke="#2f8a2a" stroke-width="2"/><path d="M6,11 L10,15 L18,5" fill="none" stroke="#2f8a2a" stroke-width="2.6" stroke-linecap="round"/></svg>Aluminium takeaway containers</li>
    <li><svg class="tick" viewBox="0 0 22 22" aria-hidden="true"><circle cx="11" cy="11" r="9" fill="none" stroke="#2f8a2a" stroke-width="2"/><path d="M6,11 L10,15 L18,5" fill="none" stroke="#2f8a2a" stroke-width="2.6" stroke-linecap="round"/></svg>Wine bottle screw tops (and collars - if you can get them off)</li>
    <li><svg class="tick" viewBox="0 0 22 22" aria-hidden="true"><circle cx="11" cy="11" r="9" fill="none" stroke="#2f8a2a" stroke-width="2"/><path d="M6,11 L10,15 L18,5" fill="none" stroke="#2f8a2a" stroke-width="2.6" stroke-linecap="round"/></svg>Tear-off can lids</li>
  </ul>
</main>
</body>
</html>
```